Cobalt Bridge Capital - Letterhead

We need letterhead options for our case funding company called Cobalt Bridge Capital. Here are some of the details:

Name - Cobalt Bridge Capital
Phone - (555) 214 - 9087
Address - 58 Harlow Lane
Suite 312
New York, NY 10482
Website - cobaltbridgecapital.example

```html
<!DOCTYPE html>
<html lang="en">
<head>
<meta charset="utf-8">
<title>Cobalt Bridge Capital – Letterhead</title>
<link href="https://fonts.googleapis.com/css2?family=Lato:wght@400;700&family=Yellowtail&display=swap" rel="stylesheet">
<style>
  :root {
    --backdrop: #d9dadb;
    --paper: #ffffff;
    --paper-shade: #f3f3f3;
    --navy: #0f4265;
    --ink: #4f4f4f;
    --ink-dark: #222222;
    --bar-one: #10375a;
    --bar-two: #5b6d7c;
    --bar-three: #8d99a3;
  }
  html, body {
    margin: 0;
    padding: 0;
    width: 1200px;
    height: 1200px;
    overflow: hidden;
    background: var(--backdrop);
  }
  .canvas {
    position: relative;
    width: 1200px;
    height: 1200px;
  }
  .letterhead {
    position: absolute;
    left: 160px;
    top: 30px;
    width: 880px;
    height: 1140px;
    background: linear-gradient(160deg, var(--paper) 40%, var(--paper-shade) 100%);
    font-family: "Lato", sans-serif;
    color: var(--ink);
    overflow: hidden;
  }
  .brand {
    position: absolute;
    top: 48px;
    left: 0;
    right: 0;
    display: flex;
    justify-content: center;
    align-items: center;
    gap: 12px;
  }
  .brand-dot {
    width: 38px;
    height: 38px;
    border-radius: 50%;
    background: var(--navy);
  }
  .brand-name {
    font-size: 20px;
    font-weight: 700;
    letter-spacing: 2px;
    text-transform: uppercase;
    color: var(--navy);
  }
  .letter {
    position: absolute;
    left: 74px;
    top: 250px;
    width: 731px;
  }
  .salutation {
    margin: 0 0 20px;
    font-size: 16.5px;
    font-weight: 700;
    color: var(--navy);
  }
  .body-copy {
    margin: 0 0 19px;
    font-size: 16.8px;
    line-height: 25.7px;
    text-align: justify;
    hyphens: manual;
  }
  .closing {
    margin: 24px 0 0;
    font-size: 19.5px;
    color: var(--ink-dark);
  }
  .signature {
    margin: 2px 0 0;
    font-family: "Yellowtail", cursive;
    font-size: 36px;
    color: var(--navy);
  }
  .contact-line {
    position: absolute;
    left: 0;
    right: 0;
    top: 1090px;
    display: flex;
    justify-content: center;
    align-items: center;
    gap: 12px;
    font-size: 13.5px;
    color: #3a3a3a;
  }
  .contact-item {
    display: inline-flex;
    align-items: center;
    gap: 5px;
  }
  .contact-icon {
    width: 14px;
    height: 14px;
  }
  .accent-bars {
    position: absolute;
    left: 0;
    right: 0;
    bottom: 0;
    height: 9px;
    display: flex;
    gap: 2px;
  }
  .accent-bar { flex: 1; }
  .accent-bar.one { background: var(--bar-one); }
  .accent-bar.two { background: var(--bar-two); }
  .accent-bar.three { background: var(--bar-three); }
</style>
</head>
<body>
<div class="canvas">
  <main class="letterhead">
    <header class="brand">
      <span class="brand-dot"></span>
      <span class="brand-name">Cobalt Bridge Capital</span>
    </header>

    <section class="letter">
      <p class="salutation">Dear Mr. Lorem,</p>
      <p class="body-copy">Lorem ipsum dolor sit amet, consectetuer adipiscing elit, sed diam nonummy nibh euismod tinci&shy;dunt ut laoreet dolore magna aliquam erat volutpat. Ut wisi enim ad minim veniam, quis nostrud exerci tation ullamcorper suscipit lobortis nisl ut aliquip ex ea commodo consequat. Duis autem vel eum iriure dolor in hendiusto odio dignissim qui blandit praesent luptatum zzril delenit augue duis dolore te feugait nulla facilisi.</p>
      <p class="body-copy">Lorem ipsum dolor sit amet, consectetuer adipiscing elit, sed diam nonummy nibh euismod tinci&shy;dunt ut laoreet dolore magna aliquam erat volutpat. Ut wisi enim ad minim veniam, quis nostrud exerci tation ullamcorper suscipit lobortis nisl ut aliquip ex ea commodo consequat. Duis autem vel eum iriure dolor in hendiusto odio dignissim qui blandit praesent luptatum zzril delenit augue duis dolore te feugait nulla facilisi.</p>
      <p class="body-copy">Lorem ipsum dolor sit amet, consectetuer adipiscing elit, sed diam nonummy nibh euismod tinci&shy;dunt ut laoreet dolore magna aliquam erat volutpat. Ut wisi enim ad minim veniam, quis nostrud exerci tation ullamcorper suscipit lobortis nisl ut aliquip ex ea commodo consequat. Duis autem vel eum iriure dolor in hendiusto odio dignissim qui blandit praesent luptatum zzril delenit augue duis dolore te feugait nulla facilisi.</p>
      <p class="closing">Sincerely Your,</p>
      <p class="signature">Your Name</p>
    </section>

    <footer class="contact-line">
      <span class="contact-item">58 Harlow Lane, Suite 312, New York, NY 10482</span>
      <span class="contact-item">
        <svg class="contact-icon" viewBox="0 0 16 16" aria-hidden="true">
          <circle cx="8" cy="8" r="7" fill="none" stroke="#555" stroke-width="1.2"/>
          <path d="M6 4.5l1.3 2-1 1c.5 1.2 1.3 2 2.4 2.5l1-1 2 1.3-.8 1.4C8 11.5 4.7 8.3 4.5 5.3z" fill="#555"/>
        </svg>
        (555) 214 - 9087
      </span>
      <span class="contact-item">
        <svg class="contact-icon" viewBox="0 0 16 16" aria-hidden="true">
          <g fill="none" stroke="#555" stroke-width="1.1">
            <circle cx="8" cy="8" r="6.8"/>
            <ellipse cx="8" cy="8" rx="3" ry="6.8"/>
            <path d="M1.2 8h13.6M2.3 4.5h11.4M2.3 11.5h11.4"/>
          </g>
        </svg>
        cobaltbridgecapital.example
      </span>
    </footer>

    <div class="accent-bars">
      <span class="accent-bar one"></span>
      <span class="accent-bar two"></span>
      <span class="accent-bar three"></span>
    </div>
  </main>
</div>
</body>
</html>
```